Amber Lark Prints

wall art that with words that inspire and can uplift people in their homes in times when they are down. An ever present presence to inspire that the subconscious takes in and subliminally feeds the home owner with positivity. Quotes... 1)In the morning, devour the prey, in the evening, divide the spoils. 2)Your situation is not your potential, but your potential depends on how you see your situation. 3)It is never too late, if your still here, then there is still time. 4)Busy your mind with the concepts of harmony, health, peace, and good will, and wonders will happen in your life. 5), it is hard to think straight while going around in circles. 6)you have everything you need to proceed. thses are just a few examples.
I would like to have colourful backgrounds. I am starting a online poster store and need a series of beautifully designed words and colours or pictures that go together like a song and it's two elements of words and music.

Target Market(s)

Anybody with a wall that wants an uplifting presence

Industry/Entity Type

Wall art, home decor

Font styles to use
Serif
Other font styles liked:
• stencil, Dead kansas, newspaper headline styles

Requirements
Must have
• I got to put that on my wall, it's amazing
Nice to have
• I am a martial artist, music producer, writer, lyricist that likes to inspire, and I also appreciate nature and beauty, how this can be incorporated into an artistic expression would be ideal elements. maybe also the colours of

```html
<!DOCTYPE html>
<html lang="en">
<head>
<meta charset="utf-8">
<title>Busy Your Mind — Wall Poster</title>
<link rel="stylesheet" href="https://fonts.googleapis.com/css2?family=Bebas+Neue&family=Permanent+Marker&family=Belleza&display=swap">
<style>
  :root {
    --poster-red: #e4202b;
    --accent-lime: #cfdf2b;
    --ink-white: #ffffff;
  }
  html, body {
    margin: 0;
    padding: 0;
    width: 848px;
    height: 1200px;
    overflow: hidden;
    background: var(--poster-red);
  }
  .poster {
    display: block;
    width: 848px;
    height: 1200px;
  }
  .poster__background { fill: var(--poster-red); }
  .poster__bar { fill: var(--accent-lime); }
  .quote-intro {
    font-family: "Permanent Marker", "Marker Felt", cursive;
    font-size: 60px;
    fill: var(--ink-white);
  }
  .quote-keyword {
    font-family: "Bebas Neue", "Arial Narrow", sans-serif;
    font-size: 180px;
    fill: var(--ink-white);
  }
  .quote-keyword__comma { fill: var(--accent-lime); }
  .quote-outro {
    font-family: "Belleza", "Optima", sans-serif;
    font-size: 56px;
    fill: var(--ink-white);
    stroke: var(--ink-white);
    stroke-width: 0.8px;
  }
</style>
</head>
<body>
<svg class="poster" viewBox="0 0 848 1200" xmlns="http://www.w3.org/2000/svg" role="img"
     aria-label="Busy your mind with the concepts of harmony, health, peace, and good will and wonders will happen in your life">
  <rect class="poster__background" x="0" y="0" width="848" height="1200"/>
  <rect class="poster__bar" x="82" y="0" width="703" height="17"/>
  <rect class="poster__bar" x="82" y="1184" width="703" height="16"/>

  <g class="quote-intro-group">
    <text class="quote-intro" x="182" y="262" textLength="480" lengthAdjust="spacingAndGlyphs">BUSY YOUR MIND</text>
    <text class="quote-intro" x="118" y="330" textLength="609" lengthAdjust="spacingAndGlyphs">WITH THE CONCEPTS OF</text>
  </g>

  <g class="quote-keywords">
    <text class="quote-keyword" x="133" y="472" textLength="587" lengthAdjust="spacingAndGlyphs">HARMONY<tspan class="quote-keyword__comma">,</tspan></text>
    <text class="quote-keyword" x="192" y="612" textLength="473" lengthAdjust="spacingAndGlyphs">HEALTH<tspan class="quote-keyword__comma">,</tspan></text>
    <text class="quote-keyword" x="103" y="754" textLength="632" lengthAdjust="spacingAndGlyphs">PEACE<tspan class="quote-keyword__comma">,</tspan> AND</text>
    <text class="quote-keyword" x="133" y="914" textLength="582" lengthAdjust="spacingAndGlyphs">GOOD WILL</text>
  </g>

  <g class="quote-outro-group">
    <text class="quote-outro" x="130" y="984" textLength="588" lengthAdjust="spacingAndGlyphs">AND WONDERS WILL</text>
    <text class="quote-outro" x="122" y="1039" textLength="605" lengthAdjust="spacingAndGlyphs">HAPPEN IN YOUR LIFE</text>
  </g>
</svg>
</body>
</html>
```